Coastal Pulse Fiesta wordpress website

We need a wordpress design for a Brazilian dance festival event to happen in mid August in Sydney Australia.

The elevator pitch for this event is:

"Coastal Pulse Fiest is for the Social dancer who loves Brazilian rhythms and wants to have a space to dance, socialize and be inspired by a more intense experience than a regular class. As opposed to congress & festivals where there is a formality and focus on performances our events focus on relaxed and warm interactions between dance professionals and dance amateurs."

Most dances are originally from Rio de Janeiro-Brazil and we want to emphasize the cultural connection between both cities Rio (Brazil) & Sydney (Australia): beach culture, warm smiley people, love for music, dance and outdoors.

Feel free to contrast flag colours red/white/blue (Australia) & Green/yellow (Brazil)

We do not have a logo and the template / theme will be hosted on Wordpress 3.5.2
Updates

Project Deadline Extended
Reason: We still havent found anything we like and some professionals have asked more time to provide a 2nd design.

Hi everyone,

Just to let you know we've extended the deadline on this design project.

Good luck

Hi please

1. use the three uploaded pics of couples dancing as a primary feature in a banner across the page.
2. use the colours of brazil - greens, yellows and blues where possible if you have not used already.
3. Do the Heart in We Sway Tropic Dance as an actual heart image.

Thanks, looking forward to the revisions.

Cheers

Marcelo and Lucy

Target Market(s)

social dancers- men & women between 25 and 60 yo. The majority of participants are single.

Industry/Entity Type

Festival

Requirements
Must have
• Top menu to be editable via wordpress.
Nice to have
• The theme should be up, lively and fun, yet relaxed and informal.
Should not have
• Any images / sillouettes of samba Carnival women in Feathers.

```html
<!DOCTYPE html>
<html lang="en">
<head>
<meta charset="utf-8">
<title>Coastal Pulse Fiesta — Social Dance Festival</title>
<link rel="stylesheet" href="https://fonts.googleapis.com/css2?family=Open+Sans:wght@400;600;700&family=Josefin+Sans:wght@300;600;700&family=Bitter:ital,wght@0,400;1,400;1,700&display=swap">
<style>
  :root {
    --red: #b30d13;
    --red-deep: #8f0a0e;
    --nav: #1b1414;
    --white: #ffffff;
    --ink: #1c1c1c;
    --body-ink: #4a4a4a;
    --btn: #d9140f;
    --stripe-blue: #2a4fa3;
    --stripe-green: #2f9a3d;
    --stripe-yellow: #f3c713;
  }
  * { box-sizing: border-box; margin: 0; padding: 0; }
  html, body { width: 1200px; height: 1200px; overflow: hidden; background: var(--white); }
  body { position: relative; font-family: "Open Sans", sans-serif; }

  .site-header { position: absolute; left: 0; top: 0; width: 1200px; height: 145px; background: var(--red); }
  .brand { position: absolute; left: 105px; top: 18px; display: flex; align-items: center; gap: 20px; }
  .brand-mark { width: 92px; height: 92px; background: rgba(255,255,255,0.22); }
  .brand-name { font-family: "Open Sans", sans-serif; font-weight: 600; font-size: 34px; line-height: 34px; color: var(--white); text-transform: uppercase; }

  .stripe { position: absolute; left: 0; width: 1200px; height: 15px; }
  .stripe-top { top: 145px; }
  .stripe-foot { top: 1136px; }

  .main-nav { position: absolute; left: 0; top: 160px; width: 1200px; height: 55px; background: var(--nav); }
  .main-nav ul { list-style: none; position: relative; height: 55px; }
  .main-nav li { position: absolute; top: 0; line-height: 55px; white-space: nowrap; font-size: 16px; color: #d8d2d2; text-transform: uppercase; letter-spacing: 0.2px; }
  .main-nav li.current { color: var(--white); font-weight: 700; }
  .nav-home { left: 110px; }
  .nav-event { left: 205px; }
  .nav-instructors { left: 408px; }
  .nav-timetable { left: 612px; }
  .nav-tickets { left: 737px; }
  .nav-about { left: 842px; }
  .nav-contact { left: 967px; }

  .hero { position: absolute; left: 0; top: 215px; width: 1200px; height: 473px; overflow: hidden;
    background: radial-gradient(ellipse at 78% 45%, #7a4a3a 0%, #3a2018 28%, #140a0a 60%),
                linear-gradient(90deg, #2a1608 0%, #5a3a18 25%, #1e1010 55%, #0e0a14 100%); }
  .hero-photo { position: absolute; inset: 0;
    background: radial-gradient(ellipse 260px 420px at 78% 60%, rgba(214,140,90,0.55), transparent 70%),
                radial-gradient(ellipse 380px 160px at 20% 30%, rgba(230,160,60,0.45), transparent 70%); }
  .hero-band { position: absolute; left: 0; top: 140px; width: 820px; height: 270px; background: rgba(10,6,6,0.45); }
  .hero-copy { position: absolute; left: 100px; top: 148px; color: var(--white); font-family: "Josefin Sans", sans-serif; text-transform: uppercase; white-space: nowrap; }
  .hero-title { font-weight: 600; font-size: 64px; line-height: 62px; }
  .hero-sub { font-weight: 300; font-size: 47px; line-height: 50px; }
  .hero-date { font-weight: 700; font-size: 66px; line-height: 64px; margin-top: 6px; }
  .hero-year { font-weight: 700; font-size: 92px; line-height: 86px; }
  .hero-edge { position: absolute; left: 0; bottom: 0; width: 1200px; height: 20px; }

  .content { position: absolute; left: 0; top: 688px; width: 1200px; height: 448px; }
  .art { position: absolute; left: 740px; top: 10px; width: 420px; height: 430px;
    background: radial-gradient(ellipse at 60% 50%, rgba(240,120,150,0.35), rgba(120,190,230,0.25) 45%, rgba(255,255,255,0) 72%); }
  .intro { position: absolute; left: 100px; top: 60px; width: 650px; }
  .intro h1 { font-family: "Bitter", serif; font-style: italic; font-weight: 700; font-size: 36px; color: var(--ink); line-height: 44px; }
  .intro h2 { font-family: "Bitter", serif; font-style: italic; font-weight: 400; font-size: 27px; color: var(--ink); line-height: 36px; }
  .intro p { margin-top: 28px; font-size: 12.5px; line-height: 17px; color: var(--body-ink); }

  .booking { position: absolute; left: 820px; top: 96px; width: 270px; text-align: center; }
  .booking-lead { font-family: "Bitter", serif; font-size: 24px; line-height: 30px; color: var(--ink); }
  .book-btn { display: inline-block; margin-top: 16px; width: 165px; height: 50px; border-radius: 25px; background: var(--btn);
    color: var(--white); font-family: "Bitter", serif; font-weight: 700; font-size: 26px; line-height: 50px; box-shadow: 0 3px 6px rgba(0,0,0,0.25); }
  .social { display: flex; justify-content: center; gap: 10px; margin-top: 18px; }
  .social span { width: 48px; height: 48px; border-radius: 50%; background: var(--btn); }

  .site-footer { position: absolute; left: 0; top: 1151px; width: 1200px; height: 49px; background: var(--red-deep); }
  .site-footer p { margin-left: 105px; line-height: 49px; font-size: 14px; color: #f3dede; text-transform: uppercase; }
</style>
</head>
<body>
  <header class="site-header">
    <div class="brand">
      <div class="brand-mark"></div>
      <div class="brand-name">Coastal<br>Pulse<br>Fiesta</div>
    </div>
  </header>

  <svg class="stripe stripe-top" viewBox="0 0 1200 15" preserveAspectRatio="none" aria-hidden="true">
    <rect width="1200" height="15" fill="#ffffff"/>
    <rect y="2" width="1200" height="3" fill="var(--stripe-blue)"/>
    <rect y="6" width="1200" height="3" fill="var(--stripe-yellow)"/>
    <rect y="10" width="1200" height="3" fill="var(--stripe-green)"/>
  </svg>

  <nav class="main-nav">
    <ul>
      <li class="nav-home current">Home</li>
      <li class="nav-event">Event Information</li>
      <li class="nav-instructors">Instructor Profiles</li>
      <li class="nav-timetable">Timetable</li>
      <li class="nav-tickets">Tickets</li>
      <li class="nav-about">About Us</li>
      <li class="nav-contact">Contact Us</li>
    </ul>
  </nav>

  <section class="hero">
    <div class="hero-photo" role="img" aria-label="Photo of a couple dancing Brazilian zouk in front of a blurred audience"></div>
    <div class="hero-band"></div>
    <div class="hero-copy">
      <div class="hero-title">Harbour Brazilian</div>
      <div class="hero-sub">Social Dance Festival</div>
      <div class="hero-date">22 August</div>
      <div class="hero-year">2014</div>
    </div>
    <svg class="hero-edge" viewBox="0 0 1200 20" preserveAspectRatio="none" aria-hidden="true">
      <polygon fill="#ffffff" points="0,20 0,10 20,0 40,10 60,0 80,10 100,0 120,10 140,0 160,10 180,0 200,10 220,0 240,10 260,0 280,10 300,0 320,10 340,0 360,10 380,0 400,10 420,0 440,10 460,0 480,10 500,0 520,10 540,0 560,10 580,0 600,10 620,0 640,10 660,0 680,10 700,0 720,10 740,0 760,10 780,0 800,10 820,0 840,10 860,0 880,10 900,0 920,10 940,0 960,10 980,0 1000,10 1020,0 1040,10 1060,0 1080,10 1100,0 1120,10 1140,0 1160,10 1180,0 1200,10 1200,20"/>
    </svg>
  </section>

  <main class="content">
    <div class="art" role="img" aria-label="Colourful swirling floral illustration in pink, blue and yellow"></div>
    <article class="intro">
      <h1>Lorem ipsum dolor sit amet</h1>
      <h2>consectetuer adipiscing elit</h2>
      <p>Lorem ipsum dolor sit amet, consectetuer adipiscing elit, sed diam nonummy nibh euismod tincidunt ut laoreet dolore magna aliquam erat volutpat. Ut wisi enim ad minim veniam, quis nostrud exerci tation ullamcorper suscipit lobortis nisl ut aliquip ex ea commodo consequat. Duis autem vel eum iriure dolor in hendrerit in vulputate velit esse molestie consequat, vel illum dolore eu feugiat nulla facilisis at vero eros et accumsan et iusto odio dignissim qui blandit praesent luptatum zzril delenit augue duis dolore te feugait nulla facilisi.</p>
    </article>
    <aside class="booking">
      <p class="booking-lead">Jump straight in to<br>book online!</p>
      <span class="book-btn">Book Now!</span>
      <div class="social"><span></span><span></span><span></span></div>
    </aside>
  </main>

  <svg class="stripe stripe-foot" viewBox="0 0 1200 15" preserveAspectRatio="none" aria-hidden="true">
    <rect width="1200" height="15" fill="#ffffff"/>
    <rect y="2" width="1200" height="3" fill="var(--stripe-blue)"/>
    <rect y="6" width="1200" height="3" fill="var(--stripe-yellow)"/>
    <rect y="10" width="1200" height="3" fill="var(--stripe-green)"/>
  </svg>

  <footer class="site-footer">
    <p>©2014 &nbsp;Coastal Pulse Fiesta &nbsp;&nbsp;| &nbsp;&nbsp;All rights reserved</p>
  </footer>
</body>
</html>
```